Vehicle Wrap

Looking for a new design to our electrical vans. Partial wrap , sides and back - no front. Logo , Services offered , KPB & RMO # , phone number and website. Needs to Use Vorlund logo as well.

```html
<!DOCTYPE html>
<html lang="en">
<head>
<meta charset="utf-8">
<title>Brantwell Electric – Van Wrap</title>
<link href="https://fonts.googleapis.com/css2?family=Josefin+Sans:wght@600;700&display=swap" rel="stylesheet">
<style>
  :root {
    --wrap-black: #1c1713;
    --wrap-gold: #c39a1f;
    --wrap-white: #ffffff;
    --page: #ecebe7;
    --ink: #111111;
  }
  * { margin: 0; padding: 0; box-sizing: border-box; }
  html, body { width: 684px; height: 1200px; overflow: hidden; background: var(--page); }
  body { position: relative; font-family: "Josefin Sans", sans-serif; font-weight: 700; }

  .panel { position: absolute; overflow: hidden; border-radius: 14px; background: var(--wrap-white); }
  .panel svg.shapes { position: absolute; inset: 0; width: 100%; height: 100%; }
  .side { left: 22px; width: 640px; height: 250px; }
  .side--driver { top: 28px; }
  .side--passenger { top: 312px; }
  .rear { top: 600px; left: 142px; width: 400px; height: 470px; background: var(--wrap-black); border-radius: 22px 22px 10px 10px; }

  .info { position: absolute; top: 52px; width: 200px; color: var(--wrap-gold); white-space: nowrap; }
  .side--driver .info { left: 0; text-align: left; }
  .side--passenger .info { right: 0; text-align: right; }

  .headline { font-size: 16px; letter-spacing: 0.3px; padding: 0 14px; }
  .service-band { margin-top: 6px; background: var(--wrap-gold); color: var(--wrap-black); font-size: 8px; padding: 5px 14px 3px; }
  .web { margin-top: 7px; font-size: 8.5px; font-weight: 600; padding: 0 14px; }
  .phone { margin-top: 12px; font-size: 16px; padding: 0 14px; display: flex; align-items: center; gap: 5px; }
  .side--passenger .phone { justify-content: flex-end; }
  .phone svg { width: 15px; height: 15px; flex: none; }
  .licence { margin-top: 3px; font-size: 7px; padding: 0 14px; letter-spacing: 0.2px; }

  .brand { position: absolute; display: flex; align-items: center; gap: 7px; color: var(--wrap-gold); font-size: 21px; line-height: 1.05; }
  .brand-dot { width: 12px; height: 12px; border-radius: 50%; background: var(--wrap-gold); flex: none; }
  .side--driver .brand { left: 214px; top: 100px; }
  .side--passenger .brand { left: 290px; top: 100px; }

  .partner { position: absolute; background: var(--wrap-white); border: 1px solid var(--ink); color: var(--ink); text-align: center; padding: 4px 7px 3px; white-space: nowrap; }
  .partner-name { font-size: 10px; letter-spacing: 0.5px; }
  .partner-note { font-size: 5px; font-weight: 600; margin-top: 2px; }
  .side--driver .partner { left: 530px; top: 142px; }
  .side--passenger .partner { left: 58px; top: 142px; }

  .rear .brand { left: 0; right: 0; top: 100px; justify-content: center; font-size: 28px; white-space: nowrap; }
  .rear-band { position: absolute; left: 0; right: 0; top: 196px; height: 42px; background: var(--wrap-gold); }
  .rear-info { position: absolute; left: 0; right: 0; top: 254px; text-align: center; color: var(--wrap-gold); white-space: nowrap; }
  .rear-info .headline { font-size: 15px; }
  .rear-info .service-band { display: inline-block; margin-top: 6px; font-size: 9px; padding: 5px 10px 3px; }
  .rear-info .web { font-size: 8px; }
  .rear .partner { right: 70px; top: 340px; }
  .rear-contact { position: absolute; right: 70px; top: 385px; color: var(--wrap-gold); text-align: right; white-space: nowrap; }
  .rear-contact .phone { font-size: 16px; padding: 0; justify-content: flex-end; margin-top: 0; }
  .rear-contact .licence { font-size: 7px; padding: 0; }
  .rear-seam { position: absolute; left: 199px; top: 0; bottom: 0; width: 1px; background: #2e2721; }
</style>
</head>
<body>

<section class="panel side side--driver" aria-label="Driver side wrap">
  <svg class="shapes" viewBox="0 0 640 250" preserveAspectRatio="none">
    <polygon points="0,0 395,0 345,250 0,250" fill="var(--wrap-black)"/>
    <polygon points="430,0 520,0 478,92 510,92 450,250 390,250 420,148 388,148" fill="var(--wrap-gold)"/>
  </svg>
  <div class="info">
    <p class="headline">ELECTRICAL &amp; GAS</p>
    <p class="service-band">RESIDENTIAL &amp; COMMERCIAL SERVICES</p>
    <p class="web">www.brantwellelectric.ca</p>
    <p class="phone"><svg viewBox="0 0 24 24"><circle cx="12" cy="12" r="12" fill="var(--wrap-gold)"/><path d="M8.5 6.5c.6-.4 1.3-.3 1.7.3l1 1.6c.3.5.2 1.2-.3 1.6l-.8.6c.6 1.4 1.7 2.5 3.1 3.1l.6-.8c.4-.5 1.1-.6 1.6-.3l1.6 1c.6.4.7 1.1.3 1.7-.8 1.3-2.3 1.9-3.7 1.3-3-1.2-5.3-3.5-6.5-6.5-.6-1.4 0-2.9 1.4-3.6z" fill="var(--wrap-black)"/></svg>555-014-2290</p>
    <p class="licence">KPB# 7004821 / RMO# 000518364</p>
  </div>
  <div class="brand"><span class="brand-dot"></span><span>Brantwell<br>Electric</span></div>
  <div class="partner"><p class="partner-name">VORLUND</p><p class="partner-note">SERVICE &amp; SALES</p></div>
</section>

<section class="panel side side--passenger" aria-label="Passenger side wrap">
  <svg class="shapes" viewBox="0 0 640 250" preserveAspectRatio="none">
    <g transform="translate(640,0) scale(-1,1)">
      <polygon points="0,0 395,0 345,250 0,250" fill="var(--wrap-black)"/>
      <polygon points="430,0 520,0 478,92 510,92 450,250 390,250 420,148 388,148" fill="var(--wrap-gold)"/>
    </g>
  </svg>
  <div class="info">
    <p class="headline">ELECTRICAL &amp; GAS</p>
    <p class="service-band">RESIDENTIAL &amp; COMMERCIAL SERVICES</p>
    <p class="web">www.brantwellelectric.ca</p>
    <p class="phone"><svg viewBox="0 0 24 24"><circle cx="12" cy="12" r="12" fill="var(--wrap-gold)"/><path d="M8.5 6.5c.6-.4 1.3-.3 1.7.3l1 1.6c.3.5.2 1.2-.3 1.6l-.8.6c.6 1.4 1.7 2.5 3.1 3.1l.6-.8c.4-.5 1.1-.6 1.6-.3l1.6 1c.6.4.7 1.1.3 1.7-.8 1.3-2.3 1.9-3.7 1.3-3-1.2-5.3-3.5-6.5-6.5-.6-1.4 0-2.9 1.4-3.6z" fill="var(--wrap-black)"/></svg>555-014-2290</p>
    <p class="licence">KPB# 7004821 / RMO# 000518364</p>
  </div>
  <div class="brand"><span class="brand-dot"></span><span>Brantwell<br>Electric</span></div>
  <div class="partner"><p class="partner-name">VORLUND</p><p class="partner-note">SERVICE &amp; SALES</p></div>
</section>

<section class="panel rear" aria-label="Rear doors wrap">
  <div class="rear-band"></div>
  <div class="rear-seam"></div>
  <div class="brand"><span class="brand-dot"></span><span>Brantwell Electric</span></div>
  <div class="rear-info">
    <p class="headline">ELECTRICAL &amp; GAS</p>
    <p class="service-band">RESIDENTIAL &amp; COMMERCIAL SERVICES</p>
    <p class="web">www.brantwellelectric.ca</p>
  </div>
  <div class="partner"><p class="partner-name">VORLUND</p><p class="partner-note">SERVICE &amp; SALES</p></div>
  <div class="rear-contact">
    <p class="phone"><svg viewBox="0 0 24 24"><circle cx="12" cy="12" r="12" fill="var(--wrap-gold)"/><path d="M8.5 6.5c.6-.4 1.3-.3 1.7.3l1 1.6c.3.5.2 1.2-.3 1.6l-.8.6c.6 1.4 1.7 2.5 3.1 3.1l.6-.8c.4-.5 1.1-.6 1.6-.3l1.6 1c.6.4.7 1.1.3 1.7-.8 1.3-2.3 1.9-3.7 1.3-3-1.2-5.3-3.5-6.5-6.5-.6-1.4 0-2.9 1.4-3.6z" fill="var(--wrap-black)"/></svg>555-014-2290</p>
    <p class="licence">KPB# 7004821 / RMO# 000518364</p>
  </div>
</section>

</body>
</html>
```